Real Estate Design Website

I would like to have a design for "real estate agent" website. It needs to be in a "Responsive" framework.

The design need to be suitable for different viewer from all around the world. It needs to be modern. It'd be great if there is a design for mobile and vexo/tablet (it's all under responsive framework). It needs to be easy to navigate and look modern

Target Market(s)

End user/Real estate buyers from different part of the world

Industry/Entity Type

Real Estate

Requirements
Must have
• It's for real estate agent website which is used to represent their brand/image but at the same time it also for their client which is real estate buyers
Should not have
• Should not be boring design/out of date

```html
<!DOCTYPE html>
<html lang="en">
<head>
<meta charset="utf-8">
<title>Real Estate Agent</title>
<link rel="stylesheet" href="https://fonts.googleapis.com/css2?family=Open+Sans:wght@300;400;600&family=Tinos&family=Signika:wght@600&display=swap">
<style>
  :root {
    --page-bg: #2b2b2b;
    --brand-blue: #2a8fd6;
    --ink: #1d1d1d;
    --body-grey: #6a6a6a;
    --panel-grey: #ededed;
    --white: #ffffff;
    --black: #000000;
  }
  * { box-sizing: border-box; margin: 0; padding: 0; }
  html, body { width: 1120px; height: 1200px; overflow: hidden; }
  body {
    position: relative;
    background: var(--page-bg);
    font-family: "Open Sans", Arial, sans-serif;
    color: var(--ink);
  }
  a { text-decoration: none; }
  .abs { position: absolute; }

  /* Header */
  .site-header { left: 160px; top: 0; width: 800px; height: 57px; background: var(--white); }
  .brand {
    left: 0; top: 0; width: 188px; height: 57px; background: var(--brand-blue);
    display: flex; align-items: center; padding-left: 16px;
    font: 600 19px/1 "Open Sans", sans-serif; color: var(--black); letter-spacing: -0.3px;
  }
  .main-nav { right: 54px; top: 18px; display: flex; gap: 19px; font-size: 13.5px; }
  .main-nav a { color: #333; }
  .main-nav a.is-active { color: var(--brand-blue); }
  .search-btn { right: 21px; top: 18px; width: 19px; height: 19px; background: var(--black); }

  /* Hero */
  .hero-backdrop {
    left: 302px; top: 158px; width: 514px; height: 108px;
    background: linear-gradient(to bottom, rgba(62,62,62,0) 0%, #393939 45%, #3b3b3b 100%);
  }
  .hero-backdrop-low {
    left: 175px; top: 340px; width: 770px; height: 115px;
    background: linear-gradient(to bottom, rgba(60,60,60,0), #313131);
  }
  .hero-quote {
    left: 160px; top: 283px; width: 800px; text-align: center; font-weight: 400;
    font-family: "Tinos", "Times New Roman", serif; color: var(--white);
  }
  .hero-quote .line-1 { font-size: 21.5px; line-height: 1.1; display: block; }
  .hero-quote .line-2 { font-size: 31px; line-height: 1.1; color: var(--brand-blue); display: block; }
  .slide-btn { top: 365px; width: 32px; height: 32px; background: var(--black); }
  .slide-btn svg { display: block; }

  .cta { display: flex; height: 34px; }
  .cta .cta-label {
    background: var(--brand-blue); color: var(--black);
    font: 600 19px/34px "Signika", sans-serif; padding: 0 8px;
  }
  .cta .cta-arrow { background: var(--black); width: 38px; display: flex; align-items: center; justify-content: center; }
  .cta-register { left: 794px; top: 421px; }
  .cta-register .cta-label { width: 128px; }

  /* Featured */
  .featured { left: 160px; top: 455px; width: 800px; height: 340px; background: var(--white); }
  .section-title { left: 20px; top: 20px; font-size: 29px; font-weight: 300; color: var(--brand-blue); }
  .property-card { top: 79px; width: 239px; }
  .property-photo { width: 239px; height: 106px; }
  .property-name { font-size: 16px; font-weight: 400; margin-top: 13px; }
  .property-text { font-size: 11.2px; line-height: 16.8px; color: var(--body-grey); margin-top: 6px; font-weight: 300; }
  .more-dot {
    display: inline-block; width: 11px; height: 11px; border-radius: 50%;
    background: var(--black); vertical-align: -1px; margin-left: 4px; position: relative;
  }
  .more-dot::before, .more-dot::after { content: ""; position: absolute; background: var(--white); }
  .more-dot::before { left: 2.5px; top: 5px; width: 6px; height: 1px; }
  .more-dot::after { left: 5px; top: 2.5px; width: 1px; height: 6px; }
  .more-dot.blue { background: var(--brand-blue); }

  /* News / testimonials */
  .info-band { left: 160px; top: 795px; width: 800px; height: 154px; background: var(--panel-grey); }
  .info-col { top: 20px; }
  .info-col h2 { font-size: 21px; font-weight: 300; }
  .info-col p { font-size: 11.3px; line-height: 15.2px; margin-top: 6px; letter-spacing: -0.15px; }
  .info-col a { display: inline-block; margin-top: 5px; color: var(--brand-blue); font-size: 11.8px; }

  /* Footer */
  .site-footer { left: 160px; top: 949px; width: 800px; height: 146px; background: var(--white); }
  .cta-login { left: 669px; top: 0; }
  .cta-login .cta-label { width: 76px; text-align: center; }
  .cta-login .cta-arrow { width: 32px; }
  .social-link {
    top: 54px; width: 30px; height: 31px;
    display: flex; align-items: center; justify-content: center;
    font: 600 9.5px/1 "Open Sans", sans-serif; color: var(--white);
  }
  .social-a { left: 21px; background: var(--black); }
  .social-b { left: 54px; background: #2aa6d9; }
  .social-c { left: 88px; background: #c8161d; }
  .copyright { left: 137px; top: 63px; font-size: 11px; color: #333; }
  .legal-nav { right: 162px; top: 1104px; display: flex; gap: 13px; font-size: 11.5px; }
  .legal-nav a { color: #ddd; }
  .footer-backdrop {
    left: 240px; top: 1120px; width: 640px; height: 80px;
    background: linear-gradient(to bottom, rgba(50,50,50,0), #313131);
  }
</style>
</head>
<body>

<header class="site-header abs">
  <div class="brand abs">Real Estate Agent</div>
  <nav class="main-nav abs">
    <a href="#" class="is-active">Home</a>
    <a href="#">Find Property</a>
    <a href="#">Offices</a>
    <a href="#">Associates</a>
    <a href="#">Contact</a>
  </nav>
  <div class="search-btn abs">
    <svg width="19" height="19" viewBox="0 0 19 19"><circle cx="8" cy="8" r="4.5" fill="none" stroke="#2a8fd6" stroke-width="2"/><line x1="11.3" y1="11.3" x2="15" y2="15" stroke="#2a8fd6" stroke-width="2.4"/></svg>
  </div>
</header>

<section class="hero">
  <div class="hero-backdrop abs" role="img" aria-label="Faint city skyline illustration"></div>
  <div class="hero-backdrop-low abs" role="img" aria-label="Faint city skyline backdrop"></div>
  <h1 class="hero-quote abs">
    <span class="line-1">Nam quis ligula a nibh fermentum venenatis vitae nec neque. Etiam</span>
    <span class="line-2">non felis mi Quisque feugiat,</span>
  </h1>
  <a class="slide-btn abs" style="left:515px" href="#" aria-label="Previous">
    <svg width="32" height="32" viewBox="0 0 32 32"><polyline points="19,8 12,16 19,24" fill="none" stroke="#fff" stroke-width="2"/></svg>
  </a>
  <a class="slide-btn abs" style="left:552px" href="#" aria-label="Next">
    <svg width="32" height="32" viewBox="0 0 32 32"><polyline points="13,8 20,16 13,24" fill="none" stroke="#fff" stroke-width="2"/></svg>
  </a>
  <a class="cta cta-register abs" href="#">
    <span class="cta-label">Register Now</span>
    <span class="cta-arrow"><svg width="14" height="20" viewBox="0 0 14 20"><polyline points="4,3 11,10 4,17" fill="none" stroke="#fff" stroke-width="2"/></svg></span>
  </a>
</section>

<section class="featured abs">
  <h2 class="section-title abs">Featured Property</h2>
  <article class="property-card abs" style="left:21px">
    <div class="property-photo" role="img" aria-label="Glass office towers against a blue sky" style="background:linear-gradient(160deg,#1f6fc4,#3a8ad6 55%,#7a6a50)"></div>
    <h3 class="property-name">Nam quis ligula a nibh</h3>
    <p class="property-text">Etiam non felis mi. Quisque feugiat, lectus non feugiat consectetur, purus ipsum lobortis nisl, a sollicitudin risus arcu elementum risus. Sed feugiat mollis neque.<span class="more-dot blue"></span></p>
  </article>
  <article class="property-card abs" style="left:281px">
    <div class="property-photo" role="img" aria-label="White family house with garden" style="background:linear-gradient(180deg,#e9eef2,#cfcfcf 50%,#6b7a3e)"></div>
    <h3 class="property-name">Ut volutpat ipsum ipsum</h3>
    <p class="property-text">Etiam non felis mi. Quisque feugiat, lectus non feugiat consectetur, purus ipsum lobortis nisl, a sollicitudin risus arcu elementum risus. Sed feugiat mollis neque.<span class="more-dot"></span></p>
  </article>
  <article class="property-card abs" style="left:541px">
    <div class="property-photo" role="img" aria-label="Resort apartment building with palm trees" style="background:linear-gradient(180deg,#3f82c9,#d8dde0 55%,#4f6b3a)"></div>
    <h3 class="property-name">Nam quis ligula a nibh</h3>
    <p class="property-text">Etiam non felis mi. Quisque feugiat, lectus non feugiat consectetur, purus ipsum lobortis nisl, a sollicitudin risus arcu elementum risus. Sed feugiat mollis neque.<span class="more-dot"></span></p>
  </article>
</section>

<section class="info-band abs">
  <div class="info-col abs" style="left:22px;width:232px">
    <h2>News</h2>
    <p>Mauris vel volutpat leo. Nunc non justo nunc. Donec sapien arcu, egestas at facilisis et, interdum eget mauris.</p>
    <a href="#">Read the full story <span class="more-dot blue"></span></a>
  </div>
  <div class="info-col abs" style="left:276px;width:480px">
    <h2>What Our Client Say</h2>
    <p>Mauris vel volutpat leo. Nunc non justo nunc. Donec sapien arcu, egestas at facilisis et, interdum eget mauris. vitae bibendum mauris. Vestibulum vehicula posuere hendrerit. risus vestibulum auctor. In hac habitasse platea dictumst.</p>
    <a href="#">More tesimonials <span class="more-dot blue"></span></a>
  </div>
</section>

<footer class="site-footer abs">
  <a class="cta cta-login abs" href="#">
    <span class="cta-label">Login</span>
    <span class="cta-arrow"><svg width="14" height="20" viewBox="0 0 14 20"><polyline points="4,3 11,10 4,17" fill="none" stroke="#fff" stroke-width="2"/></svg></span>
  </a>
  <a class="social-link social-a abs" href="#">Kin</a>
  <a class="social-link social-b abs" href="#">Peep</a>
  <a class="social-link social-c abs" href="#">Orb</a>
  <p class="copyright abs">Copyright Real Estate Agent 2013.All Rights Reserved.</p>
</footer>

<div class="footer-backdrop abs" role="img" aria-label="Faint city skyline backdrop"></div>
<nav class="legal-nav abs">
  <a href="#">Terms</a>
  <a href="#">Privacy</a>
  <a href="#">Contact</a>
</nav>

</body>
</html>
```